Harriet Voss Consortium - Paediatric Lower Limb Surgery Agenda Forming Collective

A 2-sided A4 leaflet to explain the research priorities in Children's Orthopaedic Surgery.
We would like this to be similar to that produced previously by the physiotherapists.

```html
<!DOCTYPE html>
<html lang="en">
<head>
<meta charset="utf-8">
<title>Our top 10 research priorities</title>
<link rel="stylesheet" href="https://fonts.googleapis.com/css2?family=Montserrat:wght@400;700;800&display=swap">
<style>
  :root {
    --mat: #98999c;
    --paper: #ffffff;
    --orange: #f9b11c;
    --lime: #d9d523;
    --sage: #9fc8ba;
    --teal: #0093a3;
    --ink-grey: #58595b;
    --year-grey: #8a8b8d;
  }
  * { margin: 0; padding: 0; box-sizing: border-box; }
  html, body { width: 1200px; height: 1200px; overflow: hidden; }
  body { background: var(--mat); font-family: "Montserrat", sans-serif; }
  .leaflet {
    position: absolute; left: 198px; top: 65px;
    width: 826px; height: 1069px; background: var(--paper);
  }
  .leaflet-title {
    position: absolute; left: 48px; top: 52px;
    font-weight: 800; font-size: 35px; letter-spacing: -0.5px;
    color: var(--teal); line-height: 1.2;
  }
  .priority {
    position: absolute; left: 48px; width: 729px; height: 72px;
    display: flex; align-items: center; overflow: hidden;
  }
  .priority--orange { background: var(--orange); color: #fff; }
  .priority--lime   { background: var(--lime);   color: var(--teal); }
  .priority--sage   { background: var(--sage);   color: var(--teal); }
  .priority--teal   { background: var(--teal);   color: #fff; }
  .priority__swoosh { position: absolute; top: 0; height: 100%; width: 110px; }
  .priority--left .priority__swoosh  { left: 0; }
  .priority--right .priority__swoosh { right: 0; }
  .priority__number {
    position: absolute; bottom: 0; font-weight: 800; font-size: 50px; line-height: 1;
  }
  .priority--left .priority__number  { left: 0; }
  .priority--right .priority__number { right: 0; }
  .priority--orange .priority__number { color: var(--orange); }
  .priority--lime .priority__number   { color: var(--lime); }
  .priority--sage .priority__number   { color: var(--sage); }
  .priority--teal .priority__number   { color: var(--teal); }
  .priority__text {
    position: relative; font-weight: 700; font-size: 16.5px; line-height: 20px; white-space: nowrap;
  }
  .priority--left .priority__text  { margin-left: 114px; }
  .priority--right .priority__text { margin-left: 23px; }
  .thanks {
    position: absolute; left: 50px; top: 932px; font-size: 14px; letter-spacing: -0.1px; color: var(--ink-grey); white-space: nowrap;
  }
  .credits {
    position: absolute; left: 50px; top: 966px; width: 640px;
    font-size: 12px; letter-spacing: -0.2px; line-height: 18px; color: var(--ink-grey); white-space: nowrap;
  }
  .year {
    position: absolute; right: 49px; top: 986px;
    font-weight: 800; font-size: 32px; line-height: 1; color: var(--year-grey);
  }
</style>
</head>
<body>
<main class="leaflet">
  <h1 class="leaflet-title">Our top 10 research priorities:</h1>

  <section class="priority priority--orange priority--left" style="top:105px">
    <svg class="priority__swoosh" viewBox="0 0 110 72" preserveAspectRatio="none"><path d="M0,0 C40,6 72,26 82,45 C60,56 30,68 10,72 L0,72 Z" fill="#fff"/></svg>
    <span class="priority__number">1</span>
    <p class="priority__text">What are the best ways to measure the outcome following lower<br>limb orthopaedic surgery in children?</p>
  </section>

  <section class="priority priority--lime priority--right" style="top:186px">
    <svg class="priority__swoosh" viewBox="0 0 110 72" preserveAspectRatio="none"><path d="M110,72 L110,0 C90,4 66,20 56,36 C46,52 20,58 0,70 L0,72 Z" fill="#fff"/></svg>
    <span class="priority__number">2</span>
    <p class="priority__text">Following orthopaedic surgery to the lower limbs, what should<br>children’s rehabilitation include, how long is it expected to<br>last and how does it affect the result of treatment?</p>
  </section>

  <section class="priority priority--sage priority--left" style="top:267px">
    <svg class="priority__swoosh" viewBox="0 0 110 72" preserveAspectRatio="none"><path d="M0,72 C20,64 50,60 72,54 C100,46 100,10 70,4 C40,0 10,6 0,8 Z" fill="#fff"/></svg>
    <span class="priority__number">3</span>
    <p class="priority__text">What is the short-term and long-term clinical and cost effectiveness<br>of orthopaedic lower limb surgery (including best timing and<br>technique) for children with Cerebral Palsy who can walk?</p>
  </section>

  <section class="priority priority--teal priority--right" style="top:348px">
    <svg class="priority__swoosh" viewBox="0 0 110 72" preserveAspectRatio="none"><path d="M110,0 L80,0 C40,10 40,36 20,52 C4,64 0,70 20,72 L110,72 Z" fill="#fff"/></svg>
    <span class="priority__number">4</span>
    <p class="priority__text">What are the short term and long term outcomes of surgery<br>compared to non-surgical care in the treatment of Perthes<br>disease of the hip?</p>
  </section>

  <section class="priority priority--lime priority--left" style="top:429px">
    <svg class="priority__swoosh" viewBox="0 0 110 72" preserveAspectRatio="none"><path d="M0,0 C40,6 70,24 70,42 C66,60 30,70 0,72 Z" fill="#fff"/></svg>
    <span class="priority__number">5</span>
    <p class="priority__text">What is the clinical and cost effectiveness of pre-operative<br>rehabilitation in children presenting with lower limb orthopaedic<br>conditions?</p>
  </section>

  <section class="priority priority--orange priority--right" style="top:510px">
    <svg class="priority__swoosh" viewBox="0 0 110 72" preserveAspectRatio="none"><path d="M110,0 C80,2 66,16 56,30 C44,48 20,58 0,68 L0,72 L110,72 Z" fill="#fff"/></svg>
    <span class="priority__number">6</span>
    <p class="priority__text">What is the short-term and long-term clinical and cost<br>effectiveness of Selective Dorsal Rhizotomy (SDR) in children<br>with Cerebral Palsy who can walk?</p>
  </section>

  <section class="priority priority--teal priority--left" style="top:591px;height:88px">
    <svg class="priority__swoosh" viewBox="0 0 110 88" preserveAspectRatio="none"><path d="M0,4 C50,0 100,6 100,34 C96,64 50,84 20,88 L0,88 Z" fill="#fff"/></svg>
    <span class="priority__number" style="bottom:12px">7</span>
    <p class="priority__text">Can surveillance and non-surgical treatment (e.g. physiotherapy,<br>botulinum toxin injections, functional electrical stimulation,<br>orthotics, casting) prevent the development of deformity requiring<br>surgery in children with Cerebral Palsy?</p>
  </section>

  <section class="priority priority--sage priority--right" style="top:688px">
    <svg class="priority__swoosh" viewBox="0 0 110 72" preserveAspectRatio="none"><path d="M110,0 L96,0 C80,12 70,34 54,50 C40,62 14,66 0,72 L110,72 Z" fill="#fff"/></svg>
    <span class="priority__number">8</span>
    <p class="priority__text">What is the best method of screening for Developmental<br>Dysplasia of the Hip (DDH) in terms of clinical and cost<br>effectiveness?</p>
  </section>

  <section class="priority priority--lime priority--left" style="top:769px">
    <svg class="priority__swoosh" viewBox="0 0 110 72" preserveAspectRatio="none"><path d="M0,72 L80,72 C100,50 96,14 60,6 C36,0 12,2 0,4 Z" fill="#fff"/></svg>
    <span class="priority__number">9</span>
    <p class="priority__text">What are the best strategies to optimise communication of<br>information between patients/carers and clinicians in order to<br>enable shared decision-making?</p>
  </section>

  <section class="priority priority--orange priority--right" style="top:850px">
    <svg class="priority__swoosh" viewBox="0 0 110 72" preserveAspectRatio="none"><path d="M110,0 C70,2 30,14 14,30 C0,44 0,64 4,72 L110,72 Z" fill="#fff"/></svg>
    <span class="priority__number" style="font-size:52px">10</span>
    <p class="priority__text">What is the best management for hip displacement in<br>children with Cerebral Palsy?</p>
  </section>

  <p class="thanks">Many thanks to all those people who helped us take this work off the ground and helped us finish it!</p>
  <p class="credits">The Northbrook Society of Young Limb Surgery<br>The Calder Bone &amp; Joint Association<br>The University of Wrenfield and the Harriet Voss Consortium, who always look for fair play in research!</p>
  <p class="year">2019</p>
</main>
</body>
</html>
```